Website Design for my Copper Distillation Equipment Business Nature Sciencey Theme

I already have a website www.halvorkettleworks.com and its a pixelmarten website builder one. But I cannot get the design right at all. I need this fixed.

I have logo. I need a redesign, for my website, the home page, that maybe I can have something similar in design- I can use as template to copy, for other pages so the whole thing matches? Look at my website so you understand I have a few pages...but most are links. Its a competition. Code has to be easy for me to implement, I am not expert.

Your advice needed..It would be a plus if I can update this myself throughout time. If I could have this explained to me too, the maintenance of it...how would I do this too..etc..pretend I am a child when you explain, if you can. I am not good with this stuff but I am smart and can learn fast.

I want a high end look. Maybe like an ivy league college-y look too, real preppy, chemistry...science-y, nature like is good, leaves, drops water, fields of wheat, lavender, etc.

I want every page to look similar, but the home page is what I want to be the main showpiece,..and I want each page have a little text section, maybe a photos section and a video section, for that market. Like a nice website. If I am not doing this right, let me know. I can work with you. Just help me, please. Let me know if I am doing this right.

When I pick my winning design, for my website, I will hire the artist one-on-one to re-design my shopping cart next. Or if I need additional help with implementing this current design, I can hire the same artist again too. I have a blog that I may want to hire the redesign as well too, but later on. My point is I am not just looking for one project here but I want to follow up with winning artist. So it would be return business for the winner.

I got my logo done here so I am repeat customer. And I have given that winning artist other design work.

Target Market(s)

Moonshine Stills I sell most, Essential Oil Business, Micro and Craft Distilleries, Canna-businesses, Alcohol Fuel

Industry/Entity Type

Business

Number of Pages Required

5+ page

Colors
ec1f27

Requirements
Must have
• The categories for the stills must be prominent and eye catching. The main photo I would like to be naturelike theme, but you can try out different things with me. I am open to ideas and suggestions. I would like this to be implemented easy and fast.
Nice to have
• My logo in it. You can use any of my photos as well from my flickr account. https://www.snapmeadow.com/photos/81720459@K07/
• Colors of my Logo...matching design.
• Maybe some basic stock photos you see would match for me..
• Chemistry like symbols for the categories, I love that.

```html
<!DOCTYPE html>
<html lang="en">
<head>
<meta charset="utf-8">
<title>Halvor Kettleworks – Copper Stills</title>
<link href="https://fonts.googleapis.com/css2?family=Open+Sans:wght@400;600;700&family=Great+Vibes&display=swap" rel="stylesheet">
<style>
:root{
  --red-deep:#6e1518;
  --red-mid:#8e2024;
  --red-light:#a8302f;
  --footer:#6a1513;
  --accent:#c62828;
  --ink:#222;
  --body:#555;
  --white:#fff;
  --rule:#e4e4e4;
}
*{box-sizing:border-box;margin:0;padding:0}
html,body{width:1200px;height:2338px;overflow:hidden;background:var(--white)}
body{font-family:"Open Sans",Arial,sans-serif;color:var(--ink)}
.page{position:relative;width:1200px;height:2338px;overflow:hidden}
.header{position:absolute;left:0;top:0;width:1200px;height:770px;
  background:radial-gradient(ellipse at 50% 0%,var(--red-light) 0%,var(--red-mid) 45%,var(--red-deep) 100%)}
.main-nav a{position:absolute;top:82px;transform:translateX(-50%);color:var(--white);
  font-size:15px;text-decoration:none;white-space:nowrap}
.brand{position:absolute;left:600px;top:93px;transform:translate(-50%,-50%);
  display:flex;align-items:center;gap:10px}
.brand-dot{width:18px;height:18px;border-radius:50%;background:var(--white);flex:none}
.brand-name{color:var(--white);font-weight:700;font-size:17px;line-height:21px;letter-spacing:1px;
  text-transform:uppercase;white-space:nowrap;text-align:left}
.tagline{position:absolute;left:0;width:1200px;top:212px;text-align:center;
  font-family:"Great Vibes",cursive;font-weight:400;color:var(--white);font-size:44px}
.categories{position:absolute;left:74px;top:312px;width:1052px;height:68px;display:flex}
.categories a{flex:1;display:flex;align-items:center;justify-content:center;text-align:center;
  color:var(--white);font-weight:700;font-size:14px;line-height:18px;text-decoration:none;
  text-transform:uppercase;border-left:1px solid rgba(255,255,255,.18)}
.categories a:first-child{border-left:none}
.slider{position:absolute;left:74px;top:386px;width:1052px;height:481px;background:var(--white);padding:10px;
  box-shadow:0 30px 40px -20px rgba(0,0,0,.55)}
.slide{width:100%;height:100%;background:linear-gradient(160deg,#3f5a33 0%,#6b7d54 35%,#8a6a4e 65%,#5b4738 100%)}
.dots{position:absolute;left:0;width:100%;bottom:22px;display:flex;justify-content:center;gap:8px}
.dots span{width:8px;height:8px;border-radius:50%;background:rgba(255,255,255,.55)}
.dots span:first-child{background:var(--white)}
.about-title{position:absolute;left:74px;top:938px;font-size:25px;font-weight:600;line-height:28px;text-transform:uppercase}
.about-text{position:absolute;left:74px;top:1004px;width:264px;font-size:14px;line-height:26px;color:var(--body)}
.video{position:absolute;left:370px;top:937px;width:754px;height:450px;
  background:linear-gradient(180deg,#4b6a45 0%,#6e7f62 45%,#8c8a80 100%)}
.play{position:absolute;left:355px;top:192px;width:54px;height:38px;border-radius:9px;background:#e52d27}
.play::after{content:"";position:absolute;left:21px;top:11px;border-left:15px solid var(--white);border-top:8px solid transparent;border-bottom:8px solid transparent}
.video-bar{position:absolute;left:0;bottom:0;width:100%;height:28px;background:#1b1b1b;
  display:flex;align-items:center;padding:0 14px;gap:18px;color:var(--white);font-size:12px}
.video-bar .progress{position:absolute;left:0;top:0;width:100%;height:3px;background:#555}
.video-bar .progress i{display:block;width:18%;height:100%;background:#cc181e}
.video-bar .right{margin-left:auto;display:flex;gap:14px}
.video-bar .right b{width:12px;height:12px;border:2px solid #ccc;border-radius:2px}
.purity-title{position:absolute;left:74px;top:1437px;font-size:25px;font-weight:600;text-transform:uppercase}
.purity-text{position:absolute;left:74px;top:1486px;width:1052px;font-size:13.4px;line-height:19.5px;color:var(--body)}
.read-more{position:absolute;left:74px;top:1590px;width:103px;height:37px;background:#ebebeb;
  color:#666;font-size:13px;display:flex;align-items:center;justify-content:center;text-transform:uppercase}
.product{position:absolute;top:1683px;width:242px}
.product-photo{width:242px;height:300px;border:1px solid var(--rule);padding:8px;background:var(--white)}
.product-photo div{width:100%;height:100%}
.product-name{margin-top:28px;font-size:15px;font-weight:600}
.buy{margin-top:22px;width:58px;height:37px;border:2px solid var(--accent);color:var(--accent);
  font-size:13px;display:flex;align-items:center;justify-content:center;text-transform:uppercase}
.footer{position:absolute;left:0;top:2139px;width:1200px;height:199px;background:var(--footer);color:var(--white)}
.footer-contact{position:absolute;top:43px;font-size:13px;white-space:nowrap}
.footer-phone{right:680px;text-align:right}
.footer-email{left:680px}
.footer-brand{position:absolute;left:600px;top:52px;transform:translate(-50%,-50%);display:flex;align-items:center;gap:7px}
.footer-brand .brand-dot{width:12px;height:12px}
.footer-brand .brand-name{font-size:11px;line-height:14px}
.footer-nav{position:absolute;top:112px;left:0;width:1200px;display:flex;justify-content:center;gap:22px;font-size:15px}
.copyright{position:absolute;top:163px;left:0;width:1200px;text-align:center;font-size:13px}
</style>
</head>
<body>
<div class="page">
  <header class="header">
    <nav class="main-nav">
      <a style="left:117px">HOME</a>
      <a style="left:218px">ABOUT US</a>
      <a style="left:347px">PHOTO GALLERY</a>
      <a style="left:464px">VIDEO</a>
      <a style="left:725px">SHOP</a>
      <a style="left:806px">BLOG</a>
      <a style="left:894px">BOOKS</a>
      <a style="left:980px">LINKS</a>
      <a style="left:1073px">CONTACT</a>
    </nav>
    <div class="brand"><span class="brand-dot"></span><span class="brand-name">Halvor<br>Kettleworks</span></div>
    <h2 class="tagline">Please Choose the Category of the Still you are looking for...</h2>
    <nav class="categories">
      <a>Stills</a><a>Essential<br>Oils</a><a>Alcohol<br>Fuel</a><a>Cannabis</a><a>Boilers</a>
      <a>Home<br>Distillers</a><a>Vodka<br>Still</a><a>Heat<br>Control</a><a>Distillery</a><a>Kits</a><a>Parts</a>
    </nav>
    <div class="slider">
      <div class="slide" role="img" aria-label="Copper column still and glass jars on a wooden deck table with oranges, forest behind"></div>
      <div class="dots"><span></span><span></span></div>
    </div>
  </header>

  <h3 class="about-title">About our<br>copper stills</h3>
  <p class="about-text">Lorem ipsum dolor sit amet, consectetur adipiscing elit, sed do eiusmod tempor incididunt ut labore et dolore magna aliqua. Ut enim ad minim veniam, quis nostrud exercitation ullamco laboris nisi ut aliquip ex ea commodo Lorem ipsum dolor sit amet, consectetur adipiscing elit, sed do eiusmod tempor incididunt ut labore et dolore magna aliqua. Ut enim ad minim veniam, quis nostrud exercitation ullamco laboris nisi ut aliquip ex ea commodo consequat.</p>

  <div class="video">
    <div style="position:absolute;inset:0 0 28px 0" role="img" aria-label="Video frame: a man demonstrating a copper still outdoors in a gravel yard"></div>
    <span class="play"></span>
    <div class="video-bar">
      <span class="progress"><i></i></span>
      <span>❚❚</span><span>▶❙</span><span>◀)</span><span>2:04 / 11:20</span>
      <span class="right"><b></b><b></b><b></b><b></b></span>
    </div>
  </div>

  <h3 class="purity-title">Purity comes from a direct connection with nature...</h3>
  <p class="purity-text">Welcome to our Website. Are you looking for a Moonshine Still? Are you a Lavender Farm? Are you wanting to distill Essential Oils on your farm and make Hydrosols too? Do you want to make an Herbal Extraction or Tincture? Do you want to start a Home Business? Are you a Micro ( small) Distillery wanting a Set up? Are you a Race Car driver looking for alternative ways to get your Ethanol? Are you a Prepper? Are you interested in Making Alcohol in times of Survival? Do you need clean radiation free Water for your community? Do you want to support Local Farmers, get back to the Source and Nature? Are you a Canna-business or 502?</p>
  <span class="read-more">Read more</span>

  <div class="product" style="left:74px">
    <div class="product-photo"><div role="img" aria-label="Copper column still on a steel keg on green grass" style="background:linear-gradient(180deg,#3e6a2e,#7a9a5a 60%,#b9bcb6)"></div></div>
    <p class="product-name">Home Distiller</p><span class="buy">Buy</span>
  </div>
  <div class="product" style="left:345px">
    <div class="product-photo"><div role="img" aria-label="Copper column with blue tubing on a steel pot outdoors" style="background:linear-gradient(180deg,#2f5a26,#5d8a45 60%,#a7aaa2)"></div></div>
    <p class="product-name">Essential Oil Distiller</p><span class="buy">Buy</span>
  </div>
  <div class="product" style="left:614px">
    <div class="product-photo"><div role="img" aria-label="Distillery kit with buckets in front of a house window" style="background:linear-gradient(180deg,#b8a988,#8e8b6c 55%,#5f6b45)"></div></div>
    <p class="product-name">Distillery Kit</p><span class="buy">Buy</span>
  </div>
  <div class="product" style="left:883px">
    <div class="product-photo"><div role="img" aria-label="Copper column on an electric boiler on a porch" style="background:linear-gradient(180deg,#6e8a70,#a39275 55%,#7a6552)"></div></div>
    <p class="product-name">Witch</p><span class="buy">Buy</span>
  </div>

  <footer class="footer">
    <span class="footer-contact footer-phone">+1 888 888 8888</span>
    <div class="footer-brand"><span class="brand-dot"></span><span class="brand-name">Halvor<br>Kettleworks</span></div>
    <span class="footer-contact footer-email">info@halvorkettleworks.com</span>
    <nav class="footer-nav"><span>HOME</span><span>ABOUT US</span><span>PHOTOGALLERY</span><span>VIDEO</span><span>SHOP</span><span>BLOG</span><span>BOOKS</span><span>LINKS</span><span>CONTACT US</span></nav>
    <p class="copyright">© 2015 Halvor Kettleworks - All Rights Reserved</p>
  </footer>
</div>
</body>
</html>
```